Design a premium label for the most expensive honey in the world: Manuka honey.

Manuka honey is originaire from New Zealand and recognized for its natural antibacterial activity. Rare and expensive, it is used in hospital as medical grade mainly to cure burns and wounds... Household will use it out of a pot like a "supplement" or to cure all sorts of ailments.
The label must feel:
- Premium and elegant .
- Reflect strongly its origin New Zealand. Use maori design but be careful of copyright. Must be styled.
- Purity and trust it is the real deal. Feel strongly that it is not an ersatz...
- Health and "medical" use.
Label must have:
* Brand: WAREMU DOWNS
* MANUKA HONEY
* Made in New Zealand
* e250g
* MGO300
Target Market(s)
Export.

```html
<!DOCTYPE html>
<html lang="en">
<head>
<meta charset="utf-8">
<title>Waremu Downs Manuka Honey Label</title>
<link href="https://fonts.googleapis.com/css2?family=Playfair+Display:wght@400;700&family=Comfortaa:wght@500&family=Roboto:wght@300;500&display=swap" rel="stylesheet">
<style>
  :root {
    --paper: #f5f5f5;
    --amber: #f7b234;
    --ink: #3a3a3a;
  }
  html, body {
    margin: 0;
    padding: 0;
    width: 1200px;
    height: 1200px;
    overflow: hidden;
    background: var(--paper);
  }
  .label {
    position: relative;
    width: 1200px;
    height: 1200px;
    background: var(--paper);
  }
  .frame {
    position: absolute;
    left: 82px;
    top: 30px;
    width: 1036px;
    height: 1140px;
    border: 6px solid var(--amber);
    box-sizing: border-box;
  }
  .brand {
    position: absolute;
    top: 106px;
    left: 0;
    width: 1200px;
    text-align: center;
    font-family: "Playfair Display", serif;
    font-weight: 400;
    font-size: 42px;
    line-height: 52px;
    letter-spacing: 8px;
    color: var(--ink);
    margin: 0;
  }
  .brand-rule {
    position: absolute;
    top: 165px;
    left: 282px;
    width: 632px;
    height: 2px;
    background: var(--amber);
  }
  .origin {
    position: absolute;
    top: 180px;
    left: 0;
    width: 1200px;
    text-align: center;
    font-family: "Playfair Display", serif;
    font-weight: 700;
    font-size: 23px;
    letter-spacing: 4.5px;
    color: var(--ink);
    margin: 0;
  }
  .product {
    position: absolute;
    left: 0;
    top: 0;
  }
  .product-name {
    font-family: "Comfortaa", sans-serif;
    font-weight: 500;
    fill: var(--ink);
  }
  .product-sub {
    font-family: "Comfortaa", sans-serif;
    font-weight: 500;
    fill: var(--amber);
  }
  .product-dot { fill: var(--amber); }
  .koru-line {
    fill: none;
    stroke: var(--amber);
    stroke-width: 3;
    stroke-linecap: round;
  }
  .band {
    position: absolute;
    top: 1026px;
    height: 64px;
  }
  .band svg { display: block; }
  .band-grade { left: 82px; width: 300px; }
  .band-weight { left: 806px; width: 312px; }
  .band-text {
    position: absolute;
    top: 0;
    height: 62px;
    line-height: 62px;
    font-family: "Roboto", sans-serif;
    font-weight: 300;
    font-size: 38px;
    color: var(--ink);
    letter-spacing: -1.5px;
  }
  .band-grade .band-text { left: 74px; }
  .band-weight .band-text { right: 64px; }
  .band-text strong { font-weight: 500; }
</style>
</head>
<body>
<main class="label">
  <div class="frame"></div>

  <h1 class="brand">- WAREMU DOWNS -</h1>
  <div class="brand-rule"></div>
  <p class="origin">made and packed in New Zealand</p>

  <svg class="product" width="1200" height="1200" viewBox="0 0 1200 1200" aria-label="manuka honey">
    <circle class="product-dot" cx="300" cy="600" r="92"/>
    <text class="product-name" x="412" y="656" font-size="150" textLength="578" lengthAdjust="spacingAndGlyphs">manuka</text>
    <text class="product-sub" x="984" y="736" font-size="74" text-anchor="end">honey</text>
    <path class="koru-line" d="M412 860 C 480 820, 540 820, 600 860 S 720 900, 790 860 S 920 820, 984 860"/>
  </svg>

  <div class="band band-grade">
    <svg width="300" height="64" viewBox="0 0 300 64">
      <polygon points="0,0 295,0 264,62 0,62" fill="#f7b234"/>
    </svg>
    <span class="band-text">MGO<strong>300</strong></span>
  </div>

  <div class="band band-weight">
    <svg width="312" height="64" viewBox="0 0 312 64">
      <polygon points="31,0 312,0 312,61 0,62" fill="#f7b234"/>
    </svg>
    <span class="band-text">250g ℮</span>
  </div>
</main>
</body>
</html>
```